Rocket business card

Modern business card design, use of color is good with clean space too.

Things to include on card:

Quote: I add fuel to your optometry practice

- Eyewear Sales
- Admin Duties
- Revenue Collection
- Leadership
- Tech Adoption
- COGS Reduction
- Product Sourcing
-Medical Growth

Dalton Vessey, CEO
Glint Harbor
Text Me! 847-302-1964
dalton@glintharbor.example

```html
<!DOCTYPE html>
<html lang="en">
<head>
<meta charset="utf-8">
<title>Glint Harbor – Business Card</title>
<link href="https://fonts.googleapis.com/css2?family=Arimo:wght@400;700&display=swap" rel="stylesheet">
<style>
  :root {
    --page-bg: #262626;
    --card-bg: #000000;
    --accent: #f26a22;
    --accent-warm: #f7a21c;
    --accent-red: #e0373a;
    --text-light: #ffffff;
  }
  * { margin: 0; padding: 0; box-sizing: border-box; }
  html, body {
    width: 1200px; height: 1050px; overflow: hidden;
    background: var(--page-bg);
    font-family: "Arimo", Arial, sans-serif;
    color: var(--text-light);
  }
  .canvas { position: relative; width: 1200px; height: 1050px; }
  .card {
    position: absolute; top: 196px;
    width: 377px; height: 660px;
    background: var(--card-bg);
  }
  .card--front { left: 204px; }
  .card--back { left: 620px; }

  .brand-disc {
    position: absolute; left: 90px; top: 120px;
    width: 176px; height: 176px; border-radius: 50%;
    background: linear-gradient(90deg, var(--accent-red), var(--accent) 50%, var(--accent-warm));
  }
  .contact { position: absolute; left: 46px; top: 484px; }
  .contact__name {
    font-weight: 700; font-size: 27px; color: var(--accent);
    line-height: 1;
  }
  .contact__company { font-size: 18px; margin-top: 8px; line-height: 1; }
  .contact__lines { margin-top: 30px; font-size: 18px; line-height: 25px; }
  .label { color: var(--accent); }

  .services {
    position: absolute; top: 56px; left: 0; width: 100%;
    list-style: none; text-align: center;
    font-size: 18px; line-height: 23.5px;
  }
  .services li::before { content: "- "; color: var(--accent); }

  .wordmark {
    position: absolute; left: 0; top: 500px; width: 100%;
    display: flex; flex-direction: column; align-items: center;
  }
  .wordmark__disc {
    width: 56px; height: 56px; border-radius: 50%;
    background: var(--accent);
  }
  .wordmark__name {
    margin-top: 14px; font-size: 32px; font-weight: 400;
    letter-spacing: 1px; color: var(--text-light);
  }
</style>
</head>
<body>
<div class="canvas">
  <section class="card card--front">
    <div class="brand-disc" role="img" aria-label="Glint Harbor brand disc"></div>
    <div class="contact">
      <p class="contact__name">DALTON VESSEY, CEO</p>
      <p class="contact__company">Glint Harbor</p>
      <p class="contact__lines">
        <span class="label">Text Me!</span> 847-302-1964<br>
        <span class="label">Email:</span> dalton@glintharbor.example
      </p>
    </div>
  </section>

  <section class="card card--back">
    <ul class="services">
      <li>Eyewear Sales</li>
      <li>Admin Duties</li>
      <li>Revenue Collection</li>
      <li>Leadership</li>
      <li>Tech Adoption</li>
      <li>COGS Reduction</li>
      <li>Product Sourcing</li>
      <li>Medical Growth</li>
    </ul>
    <div class="wordmark">
      <div class="wordmark__disc"></div>
      <p class="wordmark__name">GLINT HARBOR</p>
    </div>
  </section>
</div>
</body>
</html>
```